Stonebell Inc Ad Design, trying to attract new customers

Please see attached pictures and files for information
We are a Class A - Residential General Contractor in Lynchburg, VA with Master HVAC and Master PLUMBING Licenses. We focus on Water and Air Solutions for property owners.
We build, remodel, and repair homes
We do HVAC, including Humidity Control and Air Purification
We do Plumbing
We love to fix Water Leaks for Plumbing, Roof Leaks, Skylight Leaks, Basement Leaks, Foundation Leaks, Door and Window Leaks
We solve water and air issues on the outside of properties with custom structures, grading, and landscaping

Target Market(s)

Residential and Light Commercial property owners

Industry/Entity Type

Construction

Font styles to use
Other font styles liked:
• see cards

Colors
0054AA
0677BA
7BADD7
CADEEF
E8F1F8
00AB8E
00BBA5
67D7C9
C6EFE9
E9F9F6

Requirements
Must have
• See business cards
Nice to have
• see business cards
Should not have
• My name

```html
<!DOCTYPE html>
<html lang="en">
<head>
<meta charset="utf-8">
<title>Stonebell Inc Billboard</title>
<link rel="stylesheet" href="https://fonts.googleapis.com/css2?family=Anton&family=Montserrat:wght@400;500;600;700&family=Oswald:wght@600&display=swap">
<style>
  :root {
    --page-bg: #2e2e2e;
    --green-dark: #177a3a;
    --green-mid: #2e8b3c;
    --green-light: #62b040;
    --green-bright: #5fad3f;
    --white: #ffffff;
    --ink: #111111;
    --blue: #1a86cc;
  }
  html, body {
    margin: 0;
    padding: 0;
    width: 1085px;
    height: 1200px;
    overflow: hidden;
    background: var(--page-bg);
  }
  .billboard {
    position: absolute;
    left: 43px;
    top: 361px;
    width: 1000px;
    height: 478px;
    box-shadow: -14px 22px 30px rgba(0,0,0,0.55);
  }
  .billboard svg { display: block; width: 100%; height: 100%; }
  .billboard text { white-space: pre; }
  .headline {
    font-family: "Anton", "Oswald", sans-serif;
    font-size: 86px;
    fill: var(--white);
  }
  .headline-shadow { fill: var(--ink); }
  .services {
    font-family: "Montserrat", sans-serif;
    font-weight: 400;
    font-size: 62px;
    fill: var(--white);
  }
  .tagline {
    font-family: "Montserrat", sans-serif;
    font-weight: 600;
    font-size: 54px;
    fill: var(--white);
  }
  .website {
    font-family: "Montserrat", sans-serif;
    font-weight: 600;
    font-size: 42px;
    fill: var(--white);
  }
  .phone-number {
    font-family: "Oswald", sans-serif;
    font-weight: 600;
    font-size: 104px;
    fill: var(--blue);
  }
  .brand-name {
    font-family: "Montserrat", sans-serif;
    font-weight: 700;
    font-size: 66px;
    fill: var(--blue);
  }
</style>
</head>
<body>
<div class="billboard">
  <svg viewBox="0 0 1443 690" xmlns="http://www.w3.org/2000/svg">
    <defs>
      <linearGradient id="panelGreen" x1="0" y1="1" x2="1" y2="0">
        <stop offset="0" stop-color="var(--green-dark)"/>
        <stop offset="0.55" stop-color="var(--green-mid)"/>
        <stop offset="1" stop-color="var(--green-bright)"/>
      </linearGradient>
    </defs>

    <rect class="panel" width="1443" height="690" fill="url(#panelGreen)"/>

    <path class="wave-band" fill="var(--green-light)"
      d="M0 0 H720 C805 0 820 170 762 255 C700 345 560 392 380 397 C220 402 80 410 0 418 Z"/>
    <path class="wave-white" fill="var(--white)"
      d="M0 0 H700 C785 0 795 150 742 232 C690 318 555 358 380 364 C220 369 80 378 0 392 Z"/>

    <g class="brand">
      <circle cx="128" cy="228" r="30" fill="var(--blue)"/>
      <text class="brand-name" x="178" y="251">Stonebell Inc</text>
    </g>

    <g class="headline" text-anchor="end">
      <text class="headline-shadow" x="1377" y="140" textLength="554" lengthAdjust="spacingAndGlyphs">WE PUT WATER</text>
      <text x="1372" y="135" textLength="554" lengthAdjust="spacingAndGlyphs">WE PUT WATER</text>
      <text class="headline-shadow" x="1377" y="235" textLength="559" lengthAdjust="spacingAndGlyphs">AND  AIR IN ITS</text>
      <text x="1372" y="230" textLength="559" lengthAdjust="spacingAndGlyphs">AND  AIR IN ITS</text>
      <text class="headline-shadow" x="1377" y="330" textLength="225" lengthAdjust="spacingAndGlyphs">PLACE</text>
      <text x="1372" y="325" textLength="225" lengthAdjust="spacingAndGlyphs">PLACE</text>
    </g>

    <g class="services" text-anchor="end">
      <text x="1375" y="415" textLength="447" lengthAdjust="spacingAndGlyphs">CLASS A RBC</text>
      <text x="1375" y="484" textLength="570" lengthAdjust="spacingAndGlyphs">PLUMBING HVAC</text>
    </g>

    <text class="tagline" x="38" y="561" textLength="627" lengthAdjust="spacingAndGlyphs">Licensed and Insured</text>

    <path class="web-strip" fill="var(--green-light)" d="M0 588 H688 L620 690 H0 Z"/>
    <path class="edge-stripe" fill="var(--green-dark)" d="M700 538 H730 L618 690 H588 Z"/>
    <path class="phone-box" fill="var(--white)" d="M730 538 H1443 V690 H618 Z"/>

    <text class="website" x="45" y="657" textLength="530" lengthAdjust="spacingAndGlyphs">StonebellBuildsVA.com</text>

    <g class="phone-icon">
      <circle cx="758" cy="617" r="35" fill="var(--blue)"/>
      <path fill="var(--white)"
        d="M744 599 c3-2 6-1 8 2 l5 8 c1 3 0 5-2 7 l-3 2 c2 5 6 9 11 11 l2-3 c2-2 5-3 7-2 l8 5 c3 2 4 5 2 8 l-3 4 c-3 3-8 4-12 2 c-12-5-22-15-27-27 c-2-4-1-9 2-12 Z"/>
      <path fill="none" stroke="var(--white)" stroke-width="3" stroke-linecap="round"
        d="M763 600 a14 14 0 0 1 12 12 M763 592 a22 22 0 0 1 20 20"/>
    </g>
    <text class="phone-number" x="1375" y="658" text-anchor="end" textLength="555" lengthAdjust="spacingAndGlyphs">555-014-2286</text>
  </svg>
</div>
</body>
</html>
```